依頼詳細
イラストでも写真でも良いので、色んな花を敷き詰めたような・・・花束のような・・・デザイン。御祝い用なのでハッピーな気分になれる明るいデザイン。栗原葉月のイメージ。
記載項目
紙箱
サイズ:W190mm×D190mm×H135mm
印刷/カラー:オフセット印刷プロセス4色 or 特4色まで
紙質:E段段ボール
希望イメージ
シンプル 複雑
単色 カラフル
暗い 明るい
日常 高級
遊び心 厳粛
未来的 伝統的
女性的 男性的
希望する色
カラフル ビビッド
納品ファイル
• 高解像度JPG (.jpg)
• イラストレーター形式 (.ai)
補足説明
ご提案頂いた皆様に

この度は弊社募集の「バースデーケーキ用デコ箱デザイン」に多数のご提案を頂きありがとうございました。これから選定作業に取り掛かりますので結果は、もうしばらくお待ちください。
ミルトワを利用させて頂くのが初めてと言う事もあり、適切なコメント等しきれなかった事をお詫び致します。
またの機会がありましたら再度良いご提案を頂ける事を期待しております。
■ 選んだ理由

kuno3142さんのデザインを採用した理由はずばり「インパクト」です。
正直弊社内でも評価が二分したのですが、当初のコンセプトの「栗原葉槻」風なテイストが女性に支持を集めたので、決断しました。

■ 提案者全員のお礼・コメント

この度は、沢山のご提案を頂きありがとうございました。
採用のデザイン以外にも、テーマを変えれば使えそうな物が多々ありました。

弊社はミルトワを利用するのが初めてと言う事もあり、適切なコメントなどできていなかった事もあるかもしれませんがご容赦ください。

またの機会がありましたら、是非ご提案お願い致します。

```html
<!DOCTYPE html>
<html lang="en">
<head>
<meta charset="utf-8">
<title>Birthday Cake Box Dieline</title>
<link rel="stylesheet" href="https://fonts.googleapis.com/css2?family=Great+Vibes&display=swap">
<style>
  :root {
    --page: #ffffff;
    --petal-light: #f6a6d2;
    --petal-mid: #ee4f9c;
    --petal-deep: #d81b72;
    --petal-pale: #f9c6e3;
    --tab-tone: #f7b4dc;
    --fold: rgba(255, 255, 255, 0.55);
    --cut: #c9c9c9;
    --window: rgba(120, 40, 110, 0.45);
    --window-core: #f4a04a;
    --badge: #6a1f7a;
    --ink: #ffffff;
  }
  html, body {
    margin: 0;
    padding: 0;
    width: 698px;
    height: 1200px;
    overflow: hidden;
    background: var(--page);
  }
  .box-dieline {
    position: relative;
    width: 698px;
    height: 1200px;
  }
  .dieline-art {
    position: absolute;
    inset: 0;
  }
  .script {
    position: absolute;
    font-family: "Great Vibes", cursive;
    color: var(--ink);
    text-align: center;
    margin: 0;
    line-height: 1.35;
  }
  .wish-top {
    left: 120px;
    top: 78px;
    width: 460px;
    font-size: 15px;
    transform: rotate(180deg);
  }
  .wish-headline {
    left: 174px;
    top: 372px;
    width: 350px;
    height: 34px;
    font-size: 25px;
    line-height: 34px;
    white-space: nowrap;
    transform: rotate(-90deg);
    transform-origin: 50% 50%;
  }
  .wish-front {
    left: 140px;
    top: 680px;
    width: 420px;
    font-size: 15px;
  }
  .tab-label {
    position: absolute;
    width: 120px;
    height: 16px;
    line-height: 16px;
    text-align: center;
    font-family: "Great Vibes", cursive;
    color: var(--ink);
    font-size: 12px;
    white-space: nowrap;
    margin: 0;
    transform-origin: 50% 50%;
  }
  .tab-label--left { left: 28px; top: 399px; transform: rotate(-90deg); }
  .tab-label--right { left: 550px; top: 399px; transform: rotate(90deg); }
</style>
</head>
<body>
<main class="box-dieline">
  <svg class="dieline-art" width="698" height="1200" viewBox="0 0 698 1200">
    <defs>
      <linearGradient id="peony-tone" x1="0" y1="0" x2="1" y2="1">
        <stop offset="0" stop-color="var(--petal-light)"/>
        <stop offset="0.35" stop-color="var(--petal-mid)"/>
        <stop offset="0.6" stop-color="var(--petal-deep)"/>
        <stop offset="0.8" stop-color="var(--petal-mid)"/>
        <stop offset="1" stop-color="var(--petal-pale)"/>
      </linearGradient>
    </defs>

    <g class="peony-photo-area" role="img" aria-label="Close-up photograph of pink peony petals covering the whole box">
      <rect x="12" y="8" width="675" height="218" rx="14" fill="url(#peony-tone)"/>
      <rect x="35" y="226" width="628" height="351" fill="url(#peony-tone)"/>
      <path d="M35 296 L14 318 L1 330 L1 484 L14 496 L35 514 Z" fill="var(--tab-tone)"/>
      <path d="M663 296 L684 318 L697 330 L697 484 L684 496 L663 514 Z" fill="var(--tab-tone)"/>
      <rect x="12" y="577" width="675" height="237" fill="url(#peony-tone)"/>
      <rect x="2" y="824" width="694" height="370" rx="10" fill="url(#peony-tone)"/>
    </g>

    <g class="fold-lines" stroke="var(--fold)" stroke-width="1" fill="none">
      <line x1="175" y1="8" x2="175" y2="1194"/>
      <line x1="524" y1="8" x2="524" y2="1194"/>
      <line x1="12" y1="226" x2="687" y2="226"/>
      <line x1="12" y1="577" x2="687" y2="577"/>
      <line x1="12" y1="814" x2="687" y2="814"/>
      <line x1="35" y1="296" x2="35" y2="514"/>
      <line x1="663" y1="296" x2="663" y2="514"/>
      <line x1="55" y1="950" x2="55" y2="1060"/>
      <line x1="643" y1="950" x2="643" y2="1060"/>
    </g>

    <g class="cut-lines" stroke="var(--cut)" stroke-width="1" fill="none">
      <rect x="12" y="8" width="675" height="218" rx="14"/>
      <rect x="2" y="824" width="694" height="370" rx="10"/>
    </g>

    <g class="window-circles">
      <circle cx="349" cy="47" r="62" fill="var(--window)"/>
      <circle cx="349" cy="221" r="62" fill="var(--window)"/>
      <circle cx="349" cy="407" r="121" fill="none" stroke="var(--fold)" stroke-width="1.5"/>
      <circle cx="349" cy="407" r="66" fill="var(--window-core)" opacity="0.9"/>
      <circle cx="349" cy="570" r="62" fill="var(--window)"/>
    </g>

    <g class="tab-badges" fill="var(--badge)">
      <ellipse cx="60" cy="407" rx="12" ry="32"/>
      <ellipse cx="638" cy="407" rx="12" ry="32"/>
    </g>
  </svg>

  <p class="script wish-top">May this birthday be just the beginning of a year filled with happy<br>memories, wonderful moments and shining dreams.</p>
  <p class="script wish-headline">Best wishes to you on your birthday.</p>
  <p class="script wish-front">May this birthday be just the beginning of a year filled with happy<br>memories, wonderful moments and shining dreams.</p>
  <p class="tab-label tab-label--left">Happy Birthday</p>
  <p class="tab-label tab-label--right">Happy Birthday</p>
</main>
</body>
</html>
```